Business Card for a mobile physiotherapy company

I need a layout for a business card for a mobile physiotherapy company.
Slogan is "Mobile Physiotherapy - Your Road To Recovery"
Phone number is 867-402-5913
Email VantrePhysio@mailbright.ca (subject to change with website)
Website www.VantrePhysio.ca
My name and credentials: Kent Vantre Kent Vantre, BSc(kin), MPT, CAFCI, IMS
Information maybe included: Direct Billing, Services including Physiotherapy, IMS, acupuncture
Maybe include facebook and instagram logos
One side with the logo clean and sharp
Other side with details, try not to look too busy, keep everything concise

```html
<!DOCTYPE html>
<html lang="en">
<head>
<meta charset="utf-8">
<title>Vantre Physio – Business Card</title>
<link rel="stylesheet" href="https://fonts.googleapis.com/css2?family=Lato:wght@400;700&family=Tinos:wght@400;700&display=swap">
<style>
  :root {
    --backdrop: #ece9e4;
    --card-green: #0d564e;
    --card-white: #ffffff;
    --brand-green: #0f5a4b;
    --brand-navy: #2c4a7c;
    --ink-light: #ffffff;
    --rule-light: rgba(255,255,255,0.75);
  }
  * { margin: 0; padding: 0; box-sizing: border-box; }
  html, body { width: 1200px; height: 900px; overflow: hidden; }
  body { background: var(--backdrop); position: relative; font-family: "Lato", Arial, sans-serif; }

  .card {
    position: absolute;
    left: 330px;
    width: 557px;
    height: 343px;
    box-shadow: 2px 3px 6px rgba(0,0,0,0.25);
    text-align: center;
  }
  .card--details { top: 90px; background: var(--card-green); color: var(--ink-light); }
  .card--brand { top: 469px; background: var(--card-white); }

  .holder {
    position: absolute; top: 64px; left: 0; right: 0;
    font-family: "Tinos", "Times New Roman", serif;
  }
  .holder__name { font-weight: 700; font-size: 20px; text-transform: uppercase; }
  .holder__credentials { font-size: 15px; }

  .divider {
    position: absolute; left: 0; right: 0;
    display: flex; align-items: center; justify-content: center; gap: 8px;
  }
  .divider::before, .divider::after {
    content: ""; display: block; width: 48px; height: 1px; background: var(--rule-light);
  }
  .divider--contact { top: 107px; }
  .divider--services { top: 201px; font-size: 16px; letter-spacing: 0.3px; }
  .divider--services::before, .divider--services::after { width: 50px; }
  .divider--social { top: 274px; }
  .divider--social::before, .divider--social::after { width: 56px; }

  .icon-tile {
    width: 19px; height: 17px; background: var(--ink-light);
    display: flex; align-items: center; justify-content: center;
  }
  .icon-tile svg { width: 13px; height: 11px; }
  .icon-row { display: flex; gap: 5px; }

  .contact-list {
    position: absolute; top: 130px; left: 0; right: 0;
    font-size: 16px; line-height: 20px; list-style: none;
  }
  .service-list {
    position: absolute; top: 222px; left: 0; right: 0;
    font-size: 16px; line-height: 20px;
  }
  .social-dot {
    width: 28px; height: 28px; border-radius: 50%; background: var(--ink-light);
  }

  .brand-mark {
    position: absolute; top: 96px; left: 50%; transform: translateX(-50%);
    width: 60px; height: 60px; border-radius: 50%; background: var(--brand-navy);
  }
  .brand-name {
    position: absolute; top: 186px; left: 0; right: 0;
    font-family: "Lato", Arial, sans-serif; font-weight: 700;
    font-size: 42px; line-height: 1;
    color: var(--brand-green);
  }
  .tagline {
    position: absolute; top: 296px; left: 0; right: 0;
    font-size: 14.5px; color: var(--brand-green); text-transform: uppercase;
  }
</style>
</head>
<body>
  <section class="card card--details">
    <div class="holder">
      <span class="holder__name">Kent Vantre,</span>
      <span class="holder__credentials">BSC(KIN), MPT, CAFCI, IMS</span>
    </div>

    <div class="divider divider--contact">
      <div class="icon-row">
        <span class="icon-tile"><svg viewBox="0 0 13 11"><path d="M2 3 Q6.5 0 11 3 L10 5 L8 4 L8 3 Q6.5 2.2 5 3 L5 4 L3 5 Z M3 6 H10 L11 10 H2 Z" fill="#0d564e"/></svg></span>
        <span class="icon-tile"><svg viewBox="0 0 13 11"><rect x="1" y="1.5" width="11" height="8" fill="#0d564e"/><path d="M1.5 2 L6.5 6 L11.5 2" stroke="#fff" stroke-width="1" fill="none"/></svg></span>
        <span class="icon-tile"><svg viewBox="0 0 13 11"><circle cx="6.5" cy="5.5" r="5" fill="#0d564e"/><circle cx="6.5" cy="4.5" r="1.6" fill="#fff"/></svg></span>
      </div>
    </div>

    <ul class="contact-list">
      <li>867-402-5913</li>
      <li>VantrePhysio@mailbright.ca</li>
      <li>www.VantrePhysio.ca</li>
    </ul>

    <div class="divider divider--services">SERVICES</div>
    <p class="service-list">Direct Billing &nbsp;| Services including Physiotherapy<br>IMS | acupuncture</p>

    <div class="divider divider--social">
      <div class="icon-row">
        <span class="social-dot" role="img" aria-label="Social profile"></span>
        <span class="social-dot" role="img" aria-label="Social profile"></span>
      </div>
    </div>
  </section>

  <section class="card card--brand">
    <span class="brand-mark" aria-hidden="true"></span>
    <h1 class="brand-name">Vantre Physio</h1>
    <p class="tagline">Mobile Physiotherapy - Your Road to Recovery</p>
  </section>
</body>
</html>
```